Marlow Landscaping

Create a website for a new landscaping company. I have a logo already and description of services offered. I have a website that I would like all inquiries and appointments to get forwarded to. I need just need it well organized so that a husband and wife team can manage it easily. This is a company that will continue to grow over time and will need to add more services under new tabs over time. If you need the email where appointments and inquiries should go please send me a message.
Services offered are: Weekly/bi weekly mowing, weed eating and edging, Plant installation pinestraw & mulch installation, weed & feed, leaf removal and yard clean up.

```html
<!DOCTYPE html>
<html lang="en">
<head>
<meta charset="utf-8">
<title>Marlow Landscaping</title>
<link href="https://fonts.googleapis.com/css2?family=Jost:wght@400;500;600;700&family=Poppins:wght@400;500;600&family=Roboto:wght@400;500&display=swap" rel="stylesheet">
<style>
:root{
  --green-dark:#0c5a1c;
  --green:#1f7a22;
  --green-bright:#4aa02a;
  --lime:#6cbf2c;
  --yellow:#f5df12;
  --yellow-btn:#f2cf1c;
  --ink:#1c1c1c;
  --muted:#3c3c3c;
  --card:#f5f5f5;
  --mint:#eef4ec;
  --footer:#151515;
  --white:#ffffff;
}
*{margin:0;padding:0;box-sizing:border-box}
html,body{width:1200px;height:3502px;overflow:hidden;background:var(--white)}
body{position:relative;font-family:'Poppins',sans-serif;color:var(--ink)}
.abs{position:absolute}

/* header */
.site-header{position:absolute;left:0;top:0;width:1200px;height:86px;background:var(--white);z-index:3}
.nav a{position:absolute;top:34px;font-family:'Jost',sans-serif;font-size:15px;font-weight:500;color:var(--ink);text-decoration:none;letter-spacing:.3px}
.nav a.active{color:var(--green);font-weight:600}
.nav .cta{top:21px;left:953px;width:136px;height:44px;border-radius:22px;background:var(--green-dark);color:var(--white);font-weight:600;display:flex;align-items:center;justify-content:center}
.brand-badge{position:absolute;left:505px;top:-50px;width:190px;height:190px;border-radius:50%;background:var(--white);z-index:3;display:flex;flex-direction:column;align-items:center;justify-content:flex-end;padding-bottom:42px}
.brand-badge .dot{width:26px;height:26px;border-radius:50%;background:var(--green);margin-bottom:6px}
.brand-badge .name{font-family:'Jost',sans-serif;font-weight:700;font-size:22px;color:var(--green);letter-spacing:1px}

/* hero */
.hero-photo{position:absolute;left:0;top:86px;width:1200px;height:670px;background:linear-gradient(160deg,#6b5a44 0%,#5d7a3a 28%,#4e8f2a 55%,#6aa834 80%,#3f7f22 100%)}
.hero-title{position:absolute;left:113px;top:212px;font-family:'Jost',sans-serif;font-weight:600;font-size:49px;line-height:51px;color:var(--white);letter-spacing:2.5px}
.hero-copy{position:absolute;left:114px;top:374px;width:500px;font-size:15px;line-height:23px;color:var(--white)}
.btn-appoint{position:absolute;left:115px;top:460px;width:283px;height:45px;border-radius:23px;background:var(--yellow-btn);color:var(--green-dark);font-family:'Jost',sans-serif;font-weight:600;font-size:15px;display:flex;align-items:center;justify-content:center;letter-spacing:.4px}

/* about */
.green-band{position:absolute;left:0;top:0}
.about-card{position:absolute;left:80px;top:806px;width:1040px;height:454px;border-radius:20px;background:var(--card)}
.about-photo{position:absolute;left:116px;top:853px;width:374px;height:374px;border-radius:50%;background:radial-gradient(circle at 40% 40%,#7fae47,#4e8a2b 70%,#3c6f22)}
.about-title{position:absolute;left:532px;top:862px;font-family:'Jost',sans-serif;font-weight:500;font-size:31px;line-height:38px;color:var(--ink);letter-spacing:1px}
.about-copy{position:absolute;left:532px;top:957px;width:565px;font-size:14.6px;line-height:26px;color:var(--muted)}
.btn-read{position:absolute;left:532px;top:1138px;width:131px;height:44px;border-radius:22px;background:var(--green);color:var(--white);font-family:'Jost',sans-serif;font-weight:600;font-size:15px;display:flex;align-items:center;justify-content:center}

/* why choose */
.why-title{position:absolute;left:82px;top:1362px;font-family:'Jost',sans-serif;font-weight:600;font-size:32px;color:var(--white);letter-spacing:1.5px}
.feature{position:absolute;top:1428px;width:325px;height:274px;border-radius:8px;background:var(--white);text-align:center;padding-top:35px}
.feature.highlight{background:var(--yellow)}
.feature .icon{width:90px;height:90px;margin:0 auto;border-radius:50%;background:var(--green);display:flex;align-items:center;justify-content:center}
.feature h3{margin-top:22px;font-family:'Jost',sans-serif;font-weight:600;font-size:17px;letter-spacing:.6px;color:var(--ink)}
.feature p{margin:6px auto 0;width:280px;font-size:14.5px;line-height:24px;color:var(--muted)}
.feature.highlight h3{color:var(--green-dark)}
.feature.highlight p{color:var(--green-dark)}

/* services */
.section-title{position:absolute;left:0;width:1200px;text-align:center;font-family:'Jost',sans-serif;font-weight:600;font-size:31px;letter-spacing:1.5px;color:var(--green-dark)}
.section-title span{color:var(--green-bright)}
.title-rule{position:absolute;left:573px;width:54px;height:3px;background:var(--green)}
.service-photo{position:absolute;top:1980px;width:226px;height:226px;border-radius:50%}
.service-name{position:absolute;top:2222px;width:260px;text-align:center;font-family:'Jost',sans-serif;font-weight:500;font-size:15px;line-height:28px;letter-spacing:.8px;color:var(--ink)}

/* contact */
.contact-bg{position:absolute;left:0;top:2365px;width:1200px;height:700px;background:var(--mint)}
.info-icon{position:absolute;left:142px;width:62px;height:62px;border-radius:50%;background:linear-gradient(135deg,var(--green-bright),var(--green-dark));display:flex;align-items:center;justify-content:center}
.info-label{position:absolute;left:241px;font-family:'Roboto',sans-serif;font-weight:500;font-size:15px;color:var(--ink)}
.info-text{position:absolute;left:241px;font-family:'Roboto',sans-serif;font-size:14.5px;line-height:26px;color:var(--ink)}
.field{position:absolute;height:50px;background:var(--white);border:1px solid #e2e2e2;box-shadow:0 3px 8px rgba(0,0,0,.08);font-family:'Roboto',sans-serif;font-size:14px;color:#6b6b6b;padding:16px 17px}
.btn-submit{position:absolute;left:483px;top:2795px;width:130px;height:42px;border-radius:21px;background:var(--green-dark);color:var(--white);font-family:'Jost',sans-serif;font-weight:600;font-size:16px;display:flex;align-items:center;justify-content:center;letter-spacing:.6px}

/* footer */
.footer-brand{position:absolute;left:113px;top:3120px;width:272px;text-align:center}
.footer-brand .dot{width:120px;height:120px;border-radius:50%;background:var(--green);margin:0 auto 16px}
.footer-brand .name{font-family:'Jost',sans-serif;font-weight:700;font-size:40px;color:var(--green-bright);letter-spacing:3px}
.footer-head{position:absolute;top:3118px;font-family:'Jost',sans-serif;font-weight:500;font-size:20px;color:var(--white)}
.footer-links{position:absolute;top:3158px;list-style:none;font-family:'Roboto',sans-serif;font-size:15px;color:var(--white)}
.footer-links li{height:34.4px;display:flex;align-items:center;gap:9px}
.footer-contact{position:absolute;left:887px;font-family:'Roboto',sans-serif;font-size:15px;line-height:28px;color:var(--white)}
.footer-icon{position:absolute;left:887px;width:32px;height:32px;border-radius:50%;background:var(--green-bright);display:flex;align-items:center;justify-content:center}
.footer-rule{position:absolute;left:113px;top:3392px;width:977px;height:1px;background:#3a3a3a}
.copyright{position:absolute;left:0;top:3434px;width:1200px;text-align:center;font-size:15px;font-weight:500;color:var(--white)}
</style>
</head>
<body>

<header class="site-header">
  <nav class="nav">
    <a class="active" style="left:110px">HOME</a>
    <a style="left:204px">ABOUT US</a>
    <a style="left:323px">OUR SERVICES</a>
    <a style="left:736px">BLOG</a>
    <a style="left:822px">TESTIMONIALS</a>
    <a class="cta">CONTACT US</a>
  </nav>
</header>
<div class="brand-badge"><div class="dot"></div><div class="name">MARLOW</div></div>

<!-- hero -->
<div class="hero-photo" role="img" aria-label="Gardener pushing a red lawn mower across a freshly cut green lawn beside a brick building"></div>
<svg class="abs" style="left:0;top:600px" width="1200" height="170" viewBox="0 600 1200 170">
  <defs>
    <linearGradient id="swoosh" x1="0" x2="1">
      <stop offset="0" stop-color="#3f9a26"/><stop offset=".5" stop-color="#6cbf2c"/><stop offset="1" stop-color="#1f7a22"/>
    </linearGradient>
  </defs>
  <path d="M0 770 L0 748 C 250 650 500 612 700 615 C 900 618 1080 670 1200 735 L1200 770 Z" fill="url(#swoosh)"/>
  <path d="M0 770 L0 752 C 260 672 520 640 720 645 C 900 650 1070 690 1200 742 L1200 770 Z" fill="#ffffff"/>
</svg>
<h1 class="hero-title">RELIABLE LAWN CARE.<br>CLEAN RESULTS.<br>EVERY TIME.</h1>
<p class="hero-copy">Professional landscaping services you can count on—from routine mowing to full yard cleanups. Proudly serving our local community with quality, consistency, and care.</p>
<div class="btn-appoint">SCHEDULE AN APPOINTMENT</div>

<!-- green band behind about and why-choose -->
<svg class="green-band" width="1200" height="1805" viewBox="0 0 1200 1805">
  <defs>
    <linearGradient id="band" x1="0" y1="0" x2="1" y2="0">
      <stop offset="0" stop-color="#0b5418"/><stop offset=".55" stop-color="#1d7a1f"/><stop offset="1" stop-color="#4b9f22"/>
    </linearGradient>
  </defs>
  <path d="M0 1310 C 40 1270 70 1240 90 1220 L 1100 1220 C 1130 1190 1160 1150 1200 1128 L1200 1805 L0 1805 Z" fill="url(#band)"/>
</svg>

<section>
  <div class="about-card"></div>
  <div class="about-photo" role="img" aria-label="Aerial view of a winding stepping-stone garden path through a mown lawn"></div>
  <h2 class="about-title">ABOUT<br>MARLOW LANDSCAPING</h2>
  <p class="about-copy">Nemo enim ipsam voluptatem quia voluptas sit aspernatur aut odit aut fugit, sed quia consequuntur magni dolores eos qui ratione voluptatem sequi nesciunt. Neque porro quisquam est, qui dolorem ipsum quia dolor sit amet, consectetur, adipisci velit, sed quia non numquam eius modi tempora incidunt ut labore et dolore magnam aliquam quaerat voluptatem.</p>
  <div class="btn-read">READ MORE</div>
</section>

<section>
  <h2 class="why-title">WHY CHOOSE US</h2>
  <svg class="abs" style="left:1066px;top:1368px" width="62" height="26" viewBox="0 0 62 26">
    <path d="M15 3 L6 13 L15 23" fill="none" stroke="#ffffff" stroke-width="2.4"/>
    <path d="M47 3 L56 13 L47 23" fill="none" stroke="#b8e04a" stroke-width="2.4"/>
  </svg>
  <div class="feature" style="left:82px">
    <div class="icon"></div>
    <h3>LOCALLY OWNED &amp; OPERATED</h3>
    <p>Nemo enim ipsam voluptatem quia voluptas sit aspernatur aut odit aut fugit, sed quia conse.</p>
  </div>
  <div class="feature highlight" style="left:438px">
    <div class="icon">
      <svg width="44" height="50" viewBox="0 0 44 50"><circle cx="22" cy="19" r="14" fill="none" stroke="#fff" stroke-width="2.4"/><path d="M15 19 l5 5 l9 -10" fill="none" stroke="#fff" stroke-width="2.4"/><path d="M13 30 L9 47 L16 43 L20 48 L22 34 M31 30 L35 47 L28 43 L24 48 L22 34" fill="none" stroke="#fff" stroke-width="2"/></svg>
    </div>
    <h3>RELIABLE &amp; CONSISTENT SERVICE</h3>
    <p>Nemo enim ipsam voluptatem quia voluptas sit aspernatur aut odit aut fugit, sed quia conse.</p>
  </div>
  <div class="feature" style="left:793px">
    <div class="icon"></div>
    <h3>DETAIL-ORIENTED WORK</h3>
    <p>Nemo enim ipsam voluptatem quia voluptas sit aspernatur aut odit aut fugit, sed quia conse.</p>
  </div>
</section>

<section>
  <h2 class="section-title" style="top:1882px">SERVICES <span>OFFERED ARE</span></h2>
  <div class="title-rule" style="top:1932px"></div>
  <svg class="abs" style="left:50px;top:2085px" width="28" height="28" viewBox="0 0 28 28"><circle cx="14" cy="14" r="12.5" fill="none" stroke="#222" stroke-width="1.4"/><path d="M16 8 L10 14 L16 20" fill="none" stroke="#222" stroke-width="1.6"/></svg>
  <svg class="abs" style="left:1130px;top:2085px" width="28" height="28" viewBox="0 0 28 28"><circle cx="14" cy="14" r="12.5" fill="none" stroke="#222" stroke-width="1.4"/><path d="M12 8 L18 14 L12 20" fill="none" stroke="#222" stroke-width="1.6"/></svg>

  <div class="service-photo" style="left:113px;background:linear-gradient(180deg,#c9dcef,#7fa85a 55%,#3f3f3f)" role="img" aria-label="Lawn mower on grass"></div>
  <div class="service-name" style="left:96px">WEEKLY/BI<br>WEEKLY MOWING</div>
  <div class="service-photo" style="left:363px;background:linear-gradient(180deg,#5f8f3a,#8fb45e 55%,#b9b8ae)" role="img" aria-label="Edger trimming grass along a concrete walkway"></div>
  <div class="service-name" style="left:346px">WEED EATING AND<br>EDGING</div>
  <div class="service-photo" style="left:612px;background:linear-gradient(180deg,#6b4a33,#8a6a4b 60%,#5b4230)" role="img" aria-label="Hands placing a young plant into pinestraw-covered soil"></div>
  <div class="service-name" style="left:594px">PLANT INSTALLATION<br>PINESTRAW</div>
  <div class="service-photo" style="left:862px;background:linear-gradient(180deg,#d7dccf,#7a9a4a 50%,#b5662a)" role="img" aria-label="Gardener raking autumn leaves in a yard"></div>
  <div class="service-name" style="left:844px">LEAF REMOVAL AND<br>YARD CLEAN UP</div>
</section>

<section>
  <div class="contact-bg"></div>
  <h2 class="section-title" style="top:2448px">CONTACT <span>US</span></h2>
  <div class="title-rule" style="top:2498px"></div>

  <div class="info-icon" style="top:2537px"><svg width="26" height="20" viewBox="0 0 26 20"><rect x="1" y="1" width="24" height="18" rx="2" fill="#fff"/><path d="M2 3 L13 11 L24 3" fill="none" stroke="#1f7a22" stroke-width="2"/></svg></div>
  <div class="info-label" style="top:2548px">EMAIL:</div>
  <div class="info-text" style="top:2569px">info@companyname.com</div>

  <div class="info-icon" style="top:2642px"><svg width="26" height="26" viewBox="0 0 24 24"><path d="M6.6 10.8a15 15 0 0 0 6.6 6.6l2.2-2.2a1 1 0 0 1 1-.25 11.4 11.4 0 0 0 3.6.57 1 1 0 0 1 1 1V20a1 1 0 0 1-1 1A17 17 0 0 1 3 4a1 1 0 0 1 1-1h3.5a1 1 0 0 1 1 1c0 1.25.2 2.45.57 3.6a1 1 0 0 1-.25 1z" fill="none" stroke="#fff" stroke-width="1.6"/></svg></div>
  <div class="info-label" style="top:2653px">PHONE:</div>
  <div class="info-text" style="top:2674px">+1888 8888 8888</div>

  <div class="info-icon" style="top:2747px"><svg width="24" height="28" viewBox="0 0 24 28"><path d="M12 2a8 8 0 0 0-8 8c0 6 8 13 8 13s8-7 8-13a8 8 0 0 0-8-8z" fill="none" stroke="#fff" stroke-width="1.8"/><circle cx="12" cy="10" r="3" fill="none" stroke="#fff" stroke-width="1.8"/><path d="M4 25 H20" stroke="#fff" stroke-width="1.8"/></svg></div>
  <div class="info-label" style="top:2745px">ADDRESS:</div>
  <div class="info-text" style="top:2766px">418 Birchwood Ave. #204<br>Fairview, CA 92810</div>

  <div class="field" style="left:481px;top:2530px;width:282px">First Name</div>
  <div class="field" style="left:775px;top:2530px;width:282px">Last Name</div>
  <div class="field" style="left:481px;top:2593px;width:282px">Phone Number</div>
  <div class="field" style="left:775px;top:2593px;width:282px">Email</div>
  <div class="field" style="left:481px;top:2656px;width:576px;height:112px">Message</div>
  <div class="btn-submit">SUBMIT</div>
</section>

<footer>
  <svg class="abs" style="left:0;top:2900px" width="1200" height="602" viewBox="0 2900 1200 602">
    <path d="M0 2962 C 200 2900 420 2930 620 3000 C 780 3056 900 3075 1000 3060 C 1090 3048 1150 3030 1200 3015 L1200 3502 L0 3502 Z" fill="#151515"/>
  </svg>
  <div class="footer-brand"><div class="dot"></div><div class="name">MARLOW</div></div>

  <div class="footer-head" style="left:432px">Quick Links</div>
  <ul class="footer-links" style="left:432px">
    <li>➔ Home</li><li>➔ About</li><li>➔ Services</li><li>➔ Blog</li><li>➔ Contact Us</li>
  </ul>
  <div class="footer-head" style="left:641px">Help Links</div>
  <ul class="footer-links" style="left:641px">
    <li>➔ FAQ</li><li>➔ Terms of use</li><li>➔ Privacy Policy</li><li>➔ Support Links</li><li>➔ Terms &amp; Conditions</li>
  </ul>
  <div class="footer-head" style="left:887px">Contact Us</div>
  <div class="footer-icon" style="top:3156px"><svg width="14" height="18" viewBox="0 0 24 28"><path d="M12 2a8 8 0 0 0-8 8c0 6 8 14 8 14s8-8 8-14a8 8 0 0 0-8-8z" fill="#fff"/><circle cx="12" cy="10" r="3" fill="#4aa02a"/></svg></div>
  <div class="footer-contact" style="left:931px;top:3155px">MARLOW<br>United States</div>
  <div class="footer-icon" style="top:3228px"><svg width="16" height="16" viewBox="0 0 24 24"><path d="M6.6 10.8a15 15 0 0 0 6.6 6.6l2.2-2.2a1 1 0 0 1 1-.25 11.4 11.4 0 0 0 3.6.57 1 1 0 0 1 1 1V20a1 1 0 0 1-1 1A17 17 0 0 1 3 4a1 1 0 0 1 1-1h3.5a1 1 0 0 1 1 1c0 1.25.2 2.45.57 3.6a1 1 0 0 1-.25 1z" fill="#fff"/></svg></div>
  <div class="footer-contact" style="left:931px;top:3230px">+1 888 888 8888</div>
  <div class="footer-icon" style="top:3280px"><svg width="16" height="12" viewBox="0 0 26 20"><rect x="1" y="1" width="24" height="18" rx="2" fill="#fff"/><path d="M2 3 L13 11 L24 3" fill="none" stroke="#4aa02a" stroke-width="2.4"/></svg></div>
  <div class="footer-contact" style="left:931px;top:3282px">info@marlow.com</div>

  <div class="footer-rule"></div>
  <div class="copyright">Copyrights@2026.Marlow Landscaping.All Rights Reserved</div>
</footer>

</body>
</html>
```